Design some Business Cards for a company

Hi. I need professional business card.

Need to look very professional. You can use a few colors if you like.
Black, white, blue, grey preferred

Front:

COMPANY: [login to view URL] & ASSOCIATES. --- Please add this in future designs.
Name: Meenakshi Tondwal
Designation: Company Secretary
Address: 000, abcd lane, harbour park, abcd west, pune,- 411 001
Landline: 000 00000000
Mobile: +99 9999999999
Website: [login to view URL]
Email: contact@[login to view URL]

Back:
Additional Address: 000, abcd lane, harbour park, abcd west, pune,- 411 001
Mobile additional: +99 9999999999

[login to view URL] is the logo, with the description of how to use it. Please use the "CS" only as the logo.

Attached are a few samples that I like.

Thank you.

```html
<!DOCTYPE html>
<html lang="en">
<head>
<meta charset="utf-8">
<title>M.T. Vardhan &amp; Associates – Business Cards</title>
<link href="https://fonts.googleapis.com/css2?family=Roboto:wght@400;700;900&display=swap" rel="stylesheet">
<style>
  :root {
    --navy: #1f2f74;
    --navy-deep: #16235c;
    --ink: #1f2f74;
    --grey: #5a5f6e;
    --silver: #b8bcc8;
    --paper: #ffffff;
    --stage: #e9eaee;
  }
  * { margin: 0; padding: 0; box-sizing: border-box; }
  html, body { width: 1200px; height: 912px; overflow: hidden; }
  body {
    background: var(--stage);
    font-family: "Roboto", Arial, sans-serif;
    position: relative;
  }
  .card {
    position: absolute;
    width: 560px;
    height: 320px;
    border-radius: 4px;
    box-shadow: 0 6px 18px rgba(20, 30, 70, 0.18);
    overflow: hidden;
  }

  /* Back of card */
  .card-back {
    left: 80px;
    top: 90px;
    background: linear-gradient(160deg, #26388a 0%, var(--navy) 45%, var(--navy-deep) 100%);
    color: var(--paper);
  }
  .card-back .wordmark {
    position: absolute;
    left: 0; right: 0; top: 108px;
    text-align: center;
    font-weight: 900;
    font-size: 62px;
    letter-spacing: 2px;
  }
  .card-back .site {
    position: absolute;
    left: 0; right: 0; top: 220px;
    text-align: center;
    font-size: 24px;
    font-weight: 400;
  }

  /* Front of card */
  .card-front {
    left: 560px;
    top: 480px;
    background: var(--paper);
    color: var(--ink);
  }
  .card-front .band { position: absolute; left: 0; bottom: 0; }
  .card-front .identity {
    position: absolute;
    right: 40px; top: 46px;
    text-align: right;
  }
  .identity .name {
    font-weight: 700;
    font-size: 19px;
    text-transform: uppercase;
    letter-spacing: 0.5px;
  }
  .identity .title {
    font-size: 12px;
    color: var(--grey);
    margin-top: 3px;
  }
  .card-front .address {
    position: absolute;
    right: 40px; top: 100px;
    text-align: right;
    font-size: 13px;
    line-height: 17px;
    font-style: normal;
    color: var(--ink);
  }
  .address .line-first { display: inline-flex; align-items: center; gap: 6px; }
  .card-front .wordmark {
    position: absolute;
    left: 38px; top: 108px;
    font-weight: 900;
    font-size: 40px;
    color: var(--navy);
    letter-spacing: 1px;
  }
  .card-front .rule {
    position: absolute;
    left: 38px; right: 40px; top: 166px;
    height: 2px;
    background: var(--navy);
  }
  .card-front .contacts {
    position: absolute;
    left: 38px; top: 176px;
    list-style: none;
    font-size: 13px;
    line-height: 18px;
  }
  .contacts li { display: flex; align-items: center; gap: 7px; }
  .contacts svg { flex: none; }
  .card-front .company {
    position: absolute;
    right: 40px; bottom: 16px;
    color: var(--paper);
    font-weight: 700;
    font-size: 15px;
    letter-spacing: 0.5px;
  }
</style>
</head>
<body>

<section class="card card-back" aria-label="Card back">
  <div class="wordmark">VARDHAN</div>
  <div class="site">mtvardhan.com</div>
</section>

<section class="card card-front" aria-label="Card front">
  <svg class="band" width="560" height="90" viewBox="0 0 560 90" aria-hidden="true">
    <path d="M0 70 L250 70 C275 70 280 40 305 40 L560 40 L560 90 L0 90 Z" fill="var(--silver)"/>
    <path d="M0 76 L255 76 C282 76 286 48 312 48 L560 48 L560 90 L0 90 Z" fill="var(--navy)"/>
  </svg>

  <div class="identity">
    <div class="name">Meenakshi Tondwal</div>
    <div class="title">Company Secretary</div>
  </div>

  <address class="address">
    <span class="line-first">
      <svg width="12" height="11" viewBox="0 0 12 11" aria-hidden="true"><path d="M6 0.5 L11.5 5.5 L10 5.5 L10 10.5 L7.3 10.5 L7.3 7.3 L4.7 7.3 L4.7 10.5 L2 10.5 L2 5.5 L0.5 5.5 Z" fill="var(--navy)"/></svg>
      000, abcd lane,
    </span><br>
    harbour park,<br>
    abcd west, pune,- 411 001
  </address>

  <div class="wordmark">VARDHAN</div>

  <div class="rule"></div>

  <ul class="contacts">
    <li>
      <svg width="11" height="11" viewBox="0 0 12 12" aria-hidden="true"><path d="M2 1 L4.5 1 L5.5 4 L4 5 C4.7 6.6 5.4 7.3 7 8 L8 6.5 L11 7.5 L11 10 C6 10.5 1.5 6 2 1 Z" fill="var(--navy)"/></svg>
      Landline: 000 00000000
    </li>
    <li>
      <svg width="11" height="11" viewBox="0 0 12 12" aria-hidden="true"><rect x="3" y="0.5" width="6" height="11" rx="1" fill="none" stroke="var(--navy)" stroke-width="1.2"/><rect x="5" y="9" width="2" height="1" fill="var(--navy)"/></svg>
      Mobile: +99 9999999999
    </li>
    <li>
      <svg width="11" height="11" viewBox="0 0 12 12" aria-hidden="true"><rect x="0.6" y="2" width="10.8" height="8" fill="none" stroke="var(--navy)" stroke-width="1.2"/><path d="M0.6 2 L6 6.5 L11.4 2" fill="none" stroke="var(--navy)" stroke-width="1.2"/></svg>
      Email: contact@mtvardhan.com
    </li>
    <li>
      <svg width="11" height="11" viewBox="0 0 12 12" aria-hidden="true"><circle cx="6" cy="6" r="5.2" fill="none" stroke="var(--navy)" stroke-width="1.2"/><path d="M1 6 H11 M6 0.8 C3.5 3.5 3.5 8.5 6 11.2 M6 0.8 C8.5 3.5 8.5 8.5 6 11.2" fill="none" stroke="var(--navy)" stroke-width="1"/></svg>
      Website: mtvardhan.com
    </li>
  </ul>

  <div class="company">M.T.VARDHAN &amp; ASSOCIATES</div>
</section>

</body>
</html>
```